Kestrel Summit 2019 Enemies of the End-Times Church Flyer

We want a church conference flyer designed. We are looking for a professional, yet catchy design that uses our brand colors and logo creatively while communicating key information of the event effectively. <br/>The flyer must include all of the following:<br/>Title: Kestrel Summit 2019<br/>Topic: The Enemies of The End-Times Church <br/>Subtitles: <br/> -How the antichrist raises an army by social behavior engineering. <br/>-How the architects of modern social constructs escaped the church's radar. <br/>-The Holy Spirit's end-times agenda:<br/> The Knock-Out Punch!<br/>Speaker: Prophet Marcus Toliver <br/>Dates/time: December 27, 28 & 29 at 6pm<br/>Location: Halvorn Community Center <br/> 241 Pellham Street <br/> Portland, ME 04102<br/>Contact info: phone: 207-555-0148 <br/>email: contact@brookmeadow.example <br/> www.vutel.example<br/>*The flyer must also include a picture of the speaker and our Vutel logo <br/>Thanks, we look forward to seeing what you come up with!

Colors

Designer to choose colors to be used in the design.

Requirements
Must have
• The flyer must include all of the following:
• Title: Kestrel Summit 2019
• Topic: The Enemies of The End-Times Church
• Subtitles:
• -How the antichrist raises an army by social behavior engineering.
• -How the architects of modern social constructs escaped the church's radar.
• -The Holy Spirit's end-times agenda:
• The Knock-Out Punch!
• Speaker: Prophet Marcus Toliver
• Dates/time: December 27, 28 & 29 at 6pm
• Location: Halvorn Community Center
• 241 Pellham Street
• Portland, ME 04102
• Contact info: phone: 207-555-0148
• email: contact@brookmeadow.example
• www.vutel.example
• *The flyer must also include a picture of the speaker and our Vutel logo
Should not have
• Pictures of crosses or church buildings

```html
<!DOCTYPE html>
<html lang="en">
<head>
<meta charset="utf-8">
<title>Kestrel Summit 2019 – The Enemies of the End-Times Church</title>
<link rel="stylesheet" href="https://fonts.googleapis.com/css2?family=Cinzel:wght@400;700&family=Raleway:wght@400;500;600;700&display=swap">
<style>
  :root {
    --ink: #ffffff;
    --accent: #f39a1e;
    --night: #0b1518;
    --storm-warm: #6b4a26;
    --storm-mid: #2c2a22;
    --sea: #17302f;
    --frame: rgba(255,255,255,0.92);
  }
  * { margin: 0; padding: 0; box-sizing: border-box; }
  html, body { width: 777px; height: 1200px; overflow: hidden; background: var(--night); }
  .flyer {
    position: relative; width: 777px; height: 1200px; overflow: hidden;
    font-family: "Raleway", Arial, sans-serif; color: var(--ink);
  }
  .backdrop {
    position: absolute; inset: 0;
    background:
      radial-gradient(ellipse 60% 30% at 30% 22%, rgba(190,130,60,0.55), transparent 70%),
      radial-gradient(ellipse 50% 25% at 80% 15%, rgba(120,90,50,0.45), transparent 70%),
      linear-gradient(180deg, #1c1a16 0%, var(--storm-warm) 18%, var(--storm-mid) 34%, var(--sea) 52%, #10201f 70%, var(--night) 100%);
  }
  .event-name { position: absolute; top: 58px; left: 175px; font-family: "Cinzel", Georgia, serif; font-weight: 700; line-height: 1; }
  .event-name .word-a { display: block; font-size: 44px; letter-spacing: 1px; }
  .event-name .word-b { display: block; font-size: 27px; margin-top: 2px; letter-spacing: 1px; }
  .event-year { position: absolute; top: 26px; left: 366px; font-family: "Cinzel", Georgia, serif; font-size: 124px; line-height: 1; }
  .topic-frame {
    position: absolute; left: 62px; top: 168px; width: 653px; height: 246px;
    border: 2px solid var(--frame); text-align: center; font-family: "Cinzel", Georgia, serif;
  }
  .topic-main { margin-top: 20px; font-size: 86px; line-height: 1; letter-spacing: 1px; }
  .topic-join { display: flex; align-items: center; justify-content: center; gap: 18px; margin-top: 14px; font-size: 30px; line-height: 1; }
  .topic-join::before, .topic-join::after { content: ""; width: 218px; height: 2px; background: var(--ink); }
  .topic-sub { margin-top: 10px; font-size: 62px; line-height: 1; letter-spacing: 1px; }
  .sessions { position: absolute; top: 440px; left: 0; width: 777px; list-style: none; text-align: center; }
  .session { font-weight: 700; font-size: 23px; line-height: 31px; }
  .session::after { content: ""; display: block; width: 72px; height: 3px; background: var(--accent); margin: 14px auto 30px; }
  .session:nth-child(3)::after { margin-bottom: 0; }
  .detail { position: absolute; font-size: 24px; line-height: 32px; }
  .detail svg { position: absolute; left: -42px; top: 2px; }
  .detail strong { font-weight: 700; }
  .dates { left: 87px; top: 788px; }
  .dates .month { font-weight: 500; letter-spacing: 1px; }
  .time { left: 372px; top: 788px; font-weight: 700; }
  .speaker { left: 524px; top: 788px; }
  .speaker .name { display: block; color: var(--accent); font-weight: 700; font-size: 30px; line-height: 40px; }
  .venue { left: 87px; top: 886px; }
  .speaker-photo {
    position: absolute; left: 526px; top: 894px; width: 204px; height: 252px;
    border: 3px solid var(--ink);
    background: linear-gradient(160deg, #2d3a55 0%, #1a2233 55%, #0f1420 100%);
  }
  .brand-name {
    position: absolute; left: 39px; top: 1052px;
    display: flex; align-items: center; gap: 9px;
    font-family: "Cinzel", Georgia, serif; font-size: 40px; line-height: 1;
  }
  .brand-name::before { content: ""; width: 14px; height: 14px; border-radius: 50%; background: var(--accent); }
  .brand-site {
    position: absolute; left: 39px; top: 1118px;
    color: var(--accent); font-weight: 700; font-size: 25px; line-height: 30px;
  }
  .contact { position: absolute; left: 227px; top: 1056px; width: 290px; }
  .contact-label { font-weight: 700; font-size: 16px; line-height: 20px; letter-spacing: 1px; }
  .contact-phone { font-size: 35px; line-height: 44px; margin-top: 6px; }
  .contact-mail { color: var(--accent); font-size: 18px; line-height: 24px; margin-top: 6px; white-space: nowrap; }
</style>
</head>
<body>
<main class="flyer">
  <div class="backdrop" role="img" aria-label="Stormy sky with birds above a dark churning sea"></div>

  <h1 class="event-name"><span class="word-a">Kestrel</span><span class="word-b">Summit</span></h1>
  <div class="event-year">2019</div>

  <section class="topic-frame">
    <h2 class="topic-main">The Enemies</h2>
    <p class="topic-join">of the</p>
    <p class="topic-sub">End-Times Church</p>
  </section>

  <ul class="sessions">
    <li class="session">How the antichrist raises an army<br>by social behavior engineering</li>
    <li class="session">How the architects of modern social<br>constructs escaped the church's radar</li>
    <li class="session">The Holy Spirit's end-times agenda:<br>The Knock-Out Punch!</li>
  </ul>

  <div class="detail dates">
    <svg width="28" height="28" viewBox="0 0 24 24" fill="none" stroke="#f39a1e" stroke-width="2"><rect x="3" y="5" width="18" height="16" rx="1"/><path d="M3 10h18M8 3v4M16 3v4M7 14h2M11 14h2M15 14h2M7 17h2M11 17h2M15 17h2"/></svg>
    <span class="month">DECEMBER</span><br><strong>27, 28 &amp; 29</strong>
  </div>

  <div class="detail time">
    <svg width="28" height="28" viewBox="0 0 24 24" fill="none" stroke="#f39a1e" stroke-width="2.4"><circle cx="12" cy="12" r="9"/><path d="M12 7v5l3 3"/></svg>
    6PM
  </div>

  <div class="detail speaker">Speaker: <strong>Prophet</strong><span class="name">Marcus Toliver</span></div>

  <div class="detail venue">
    <svg width="26" height="30" viewBox="0 0 24 28" fill="none" stroke="#f39a1e" stroke-width="2.4"><path d="M12 26s-8-8.5-8-14a8 8 0 0 1 16 0c0 5.5-8 14-8 14z"/><circle cx="12" cy="12" r="3"/></svg>
    <strong>Halvorn Community Center</strong><br>241 Pellham Street<br>Portland, ME 04102
  </div>

  <div class="speaker-photo" role="img" aria-label="Portrait photo of the speaker, Prophet Marcus Toliver"></div>

  <div class="brand-name">Vutel</div>
  <div class="brand-site">vutel.example</div>

  <div class="contact">
    <div class="contact-label">CONTACT</div>
    <div class="contact-phone">207-555-0148</div>
    <div class="contact-mail">contact@brookmeadow.example</div>
  </div>
</main>
</body>
</html>
```